small auto electrical company needs new logo and business cards !!!

we are a small auto electrical company (Velmor Autos Ltd) that has been running for 13 years the logo we have was put together by dinosaurs so we are looking at re branding the company starting with business cards and a new logo we fit GPS tracking devices for young drivers through there insurance company also we fit hands free systems and dash cameras also safety locks to fleet vehicles we would like bright eye catching colours day glow and neon and quirky designs for the logo our original logo was baby blue which i have added a picture enclosed we would like double sided but have a space to write notes and prices preferably not white on back same colour throughout many thanks
Reason: Just a chance to finalise any designs we want VA logos or V logos - No vlm's and no dinosaurs lol
Business
Installs@velmorautos.co.uk
07922483617
www.Velmorautos.co.uk
Velmor Autos Ltd - Fleets and Insurance Services
- new logo design !!
- Satellite in logo or something attaining to gps
- maybe a car in the logo
- shouldnt have velmor as vlm it is VeLMOR Autos

```html
<!DOCTYPE html>
<html lang="en">
<head>
<meta charset="utf-8">
<title>Velmor Autos Ltd – Business Cards</title>
<link rel="stylesheet" href="https://fonts.googleapis.com/css2?family=Cinzel:wght@700&family=Cormorant+Garamond:ital,wght@1,500&family=Noto+Sans:wght@400;700&display=swap">
<style>
  :root {
    --teal: #00786c;
    --teal-deep: #006a61;
    --ink: #1f1f1f;
    --paper: #f0f0f0;
    --backdrop: #e2e2e2;
    --white: #ffffff;
  }
  * { margin: 0; padding: 0; box-sizing: border-box; }
  html, body { width: 1200px; height: 1200px; overflow: hidden; }
  body { background: var(--backdrop); position: relative; font-family: "Noto Sans", Verdana, sans-serif; }

  .card { position: absolute; width: 722px; height: 434px; overflow: hidden; }
  .card--front { left: 238px; top: 106px; background: var(--paper); }
  .card--back { left: 240px; top: 630px; background: var(--teal-deep); }

  .brand { position: absolute; display: flex; align-items: center; gap: 14px; font-family: "Cinzel", "Times New Roman", serif; font-weight: 700; }
  .brand__dot { width: 56px; height: 56px; border-radius: 50%; flex: none; }
  .brand__name { line-height: 1; }
  .brand__main { display: block; font-size: 44px; letter-spacing: 1px; }
  .brand__sub { display: block; font-size: 25px; letter-spacing: 1px; margin-top: 4px; }

  .card--front .brand { left: 67px; top: 165px; color: var(--teal); }
  .card--front .brand__dot { background: var(--teal); }
  .card--back .brand { left: 232px; top: 188px; color: var(--white); }
  .card--back .brand__dot { background: var(--white); }

  .person { position: absolute; left: 372px; top: 104px; }
  .person__name { font-weight: 700; font-size: 32px; color: var(--teal); letter-spacing: 0.5px; line-height: 1.1; }
  .person__role { font-size: 21px; color: var(--ink); letter-spacing: 0.5px; margin-top: 4px; }

  .contacts { position: absolute; left: 372px; top: 188px; list-style: none; }
  .contacts li { display: flex; align-items: center; height: 39px; font-size: 19px; color: var(--ink); letter-spacing: 0.3px; }
  .contacts svg { width: 26px; height: 26px; margin-right: 17px; flex: none; }

  .front-band { position: absolute; left: 0; bottom: 0; width: 722px; height: 42px; }

  .services { position: absolute; left: 0; right: 0; top: 320px; text-align: center; color: var(--white); font-family: "Cormorant Garamond", Georgia, serif; font-style: italic; font-weight: 500; }
  .services__title { font-size: 25px; letter-spacing: 1px; font-variant: small-caps; text-transform: uppercase; }
  .services__list { font-size: 17px; letter-spacing: 1px; font-variant: small-caps; line-height: 22px; margin-top: 4px; }
</style>
</head>
<body>

<section class="card card--front" aria-label="Business card front">
  <div class="brand">
    <span class="brand__dot"></span>
    <span class="brand__name"><span class="brand__main">Velmor</span><span class="brand__sub">Autos Ltd</span></span>
  </div>

  <div class="person">
    <p class="person__name">Jonn Doe</p>
    <p class="person__role">Project Manager</p>
  </div>

  <ul class="contacts">
    <li>
      <svg viewBox="0 0 26 26" aria-hidden="true"><circle cx="13" cy="13" r="13" fill="var(--teal)"/><path d="M8.5 7.5c.8-.8 1.7-.7 2.2.1l1 1.7c.4.7.2 1.4-.4 1.9l-.6.5c.6 1.5 1.9 2.8 3.4 3.4l.5-.6c.5-.6 1.2-.8 1.9-.4l1.7 1c.8.5.9 1.4.1 2.2l-.7.7c-1 1-3.4.6-6-2s-3-5-2-6z" fill="var(--white)"/></svg>
      079 224 83617
    </li>
    <li>
      <svg viewBox="0 0 26 26" aria-hidden="true"><circle cx="13" cy="13" r="13" fill="var(--teal)"/><rect x="7.5" y="9" width="11" height="8" fill="var(--white)"/><path d="M7.5 9l5.5 4.5 5.5-4.5M7.5 17l4-3.5M18.5 17l-4-3.5" stroke="var(--teal)" stroke-width="1" fill="none"/></svg>
      Installs@velmorautos.co.uk
    </li>
    <li>
      <svg viewBox="0 0 26 26" aria-hidden="true"><circle cx="13" cy="13" r="13" fill="var(--teal)"/><g stroke="var(--white)" stroke-width="1.1" fill="none"><circle cx="13" cy="13" r="6.5"/><ellipse cx="13" cy="13" rx="2.8" ry="6.5"/><path d="M6.5 13h13M7.5 9.7h11M7.5 16.3h11"/></g></svg>
      www.velmorautos.co.uk
    </li>
  </ul>

  <svg class="front-band" viewBox="0 0 722 42" aria-hidden="true">
    <rect width="722" height="42" fill="var(--teal)"/>
    <polygon points="210,0 722,0 722,22 236,22" fill="var(--white)"/>
    <polygon points="218,0 722,0 722,19 240,19" fill="var(--ink)"/>
  </svg>
</section>

<section class="card card--back" aria-label="Business card back">
  <div class="brand">
    <span class="brand__dot"></span>
    <span class="brand__name"><span class="brand__main">Velmor</span><span class="brand__sub">Autos Ltd</span></span>
  </div>

  <div class="services">
    <p class="services__title">Our Services</p>
    <p class="services__list">GPS Tracking Devices - Hands Free Systems<br>Dash Cameras - Safety Locks to Fleet Vehicles</p>
  </div>
</section>

</body>
</html>
```